Design + Finalize Lead Magnet

Lead Magnet:
"10 Costly Workers’ Comp Mistakes Contractors Make — and How to Avoid Them"
Create a polished, professional PDF lead magnet based on provided content. This guide will be offered as a downloadable resource to construction contractors via Pathlink, email, and our website. The purpose is to build trust, demonstrate expertise in workers’ compensation insurance, and generate qualified leads for Brelwick
Insurance.
Project Scope:
Design the Lead Magnet (8–10 pages):
Use the full text provided in the document.
Include a visually engaging cover page (title, logo, clean construction image).
Use section headers, checklists, icons, and callouts for easier reading.
Incorporate the MOD Rate Improvement Checklist as a visual checklist (bullets or checkboxes).
Create a strong call to action page at the end with contact info and a link to request a free Workers’ Comp Risk Assessment.

Style Requirements:
Professional and clean design suited to construction contractors
Use brand colors: navy, gray, white, and accent blue/teal
Fonts: Montserrat, Lato, or Open Sans (modern, easy to read)
Include space for our logo and contact info in footer or closing page

Export & Delivery:
Final product as a high-resolution PDF (optimized for web/email)
Optional: Separate Canva template link for future edits

```html
<!DOCTYPE html>
<html lang="en">
<head>
<meta charset="utf-8">
<title>Brelwick – Workers' Comp Lead Magnet Pages</title>
<link href="https://fonts.googleapis.com/css2?family=Montserrat:wght@500;600;700;800&family=Lato:wght@400;700&display=swap" rel="stylesheet">
<style>
:root{
  --navy:#0f1e3d;
  --teal:#3a8c94;
  --teal-dark:#2f7880;
  --gray:#5b5f66;
  --light:#f3f4f5;
  --white:#ffffff;
  --stage:#1d1d1f;
}
*{box-sizing:border-box;margin:0;padding:0}
html,body{width:1200px;height:691px;overflow:hidden;background:var(--stage)}
.stage{position:relative;width:1200px;height:691px}
.page{position:absolute;width:339px;height:262px;background:var(--white);overflow:hidden;font-family:'Lato',sans-serif;color:var(--gray)}
.abs{position:absolute}
.h{font-family:'Montserrat',sans-serif;color:var(--navy);font-weight:700;line-height:1.1}
.teal{color:var(--teal)}
.photo{position:absolute}
.tab{position:absolute;left:0;top:18px;height:23px;background:var(--teal);color:var(--white);font-family:'Montserrat',sans-serif;font-weight:700;font-size:13.5px;line-height:23px;padding-left:13px}
.tab-stripes{position:absolute;top:18px}
.footer-brand{position:absolute;left:14px;top:244px;display:flex;align-items:center;gap:3px;font-family:'Montserrat',sans-serif;font-weight:600;font-size:5.5px;color:var(--navy)}
.dot{width:8px;height:8px;border-radius:50%;background:var(--navy)}
.footer-line{position:absolute;left:58px;right:14px;top:250px;height:0.6px;background:var(--navy)}
.page-num{position:absolute;right:12px;top:248px;width:4px;height:4px;background:var(--teal)}
.body{font-size:6.2px;line-height:8.1px}
.label{font-weight:700;color:var(--teal)}
.avoid-title{display:flex;align-items:center;gap:3px;font-family:'Montserrat',sans-serif;font-weight:700;color:var(--teal)}
</style>
</head>
<body>
<div class="stage">

<!-- Cover -->
<section class="page cover" style="left:72px;top:73px">
  <div class="photo" role="img" aria-label="Smiling construction worker in a yellow hard hat and plaid shirt at a job site" style="left:130px;top:0;width:209px;height:262px;background:linear-gradient(160deg,#e9e9e6 0%,#c9b38a 35%,#6a6a60 70%,#3b4a52 100%);border-bottom-left-radius:150px 110px"></div>
  <div class="abs" style="left:0;top:0;width:190px;height:262px;background:linear-gradient(90deg,#ffffff 70%,rgba(255,255,255,0))"></div>
  <svg class="abs" style="left:0;top:0" width="339" height="262" viewBox="0 0 339 262">
    <path d="M210 262 C150 240 140 160 250 120 L262 130 C170 170 190 235 260 250 L339 235 L339 262 Z" fill="var(--teal)"/>
  </svg>
  <div class="abs footer-brand" style="left:19px;top:24px;font-size:13px;gap:6px"><span class="dot" style="width:15px;height:15px"></span>Brelwick</div>
  <h1 class="abs h" style="left:19px;top:81px;font-size:14.2px;font-weight:800;line-height:16px;width:210px">10 Costly Workers'<br>Comp <span class="teal">Mistakes Contractors</span><br><span class="teal">Make</span> and How to<br>Avoid Them</h1>
  <p class="abs" style="left:19px;top:153px;font-family:'Montserrat',sans-serif;font-weight:500;font-size:9px;line-height:10.8px;color:#707379;width:130px">A Practical Guide for Construction Business Owners</p>
  <div class="abs" style="left:0;top:195px;width:147px;height:49px;background:var(--navy);padding:6px 0 0 19px;color:var(--white);font-family:'Montserrat',sans-serif">
    <div style="font-size:5px">Presented by:</div>
    <div style="font-size:7.8px;font-weight:700;margin:1px 0">Marisol Vendray</div>
    <div style="font-size:4.6px;line-height:5.6px">Licensed Agent/Broker at<br>Brelwick Insurance &amp; Consulting | Workers'<br>Compensation Specialists</div>
  </div>
</section>

<!-- Introduction -->
<section class="page" style="left:430px;top:73px">
  <div class="tab" style="width:107px">Introduction</div>
  <svg class="tab-stripes" style="left:107px" width="26" height="23"><polygon points="0,0 6,0 16,23 10,23" fill="var(--navy)"/><polygon points="9,0 15,0 25,23 19,23" fill="var(--navy)"/></svg>
  <div class="photo" role="img" aria-label="Worker in a hard hat facing a timber building frame at sunset" style="left:25px;top:59px;width:131px;height:162px;border-radius:10px;background:linear-gradient(180deg,#c7a478 0%,#e8a24a 40%,#8a5a30 75%,#4a3424 100%)"></div>
  <h2 class="abs h" style="left:174px;top:58px;font-size:12.5px">Why This<br>Guide Matters</h2>
  <div class="abs body" style="left:174px;top:89px;width:128px;font-size:5.7px;text-align:justify">
    <p>As a contractor, your time, money, and reputation are on the line. Workers' compensation costs can skyrocket due to preventable mistakes—hurting your business and your bottom line. Workers' compensation can be one of the most expensive and misunderstood areas of business for contractors. One mistake—like misclassifying employees or skipping safety training—can lead to huge premium increases or denied claims.</p>
    <p style="margin-top:8px">This guide highlights the top errors contractors make and provides straightforward solutions to help you stay compliant, reduce risk, and protect your workforce.</p>
  </div>
  <div class="footer-brand"><span class="dot"></span>Brelwick</div>
  <div class="footer-line"></div><div class="page-num"></div>
</section>

<!-- Mistake 1 -->
<section class="page" style="left:790px;top:73px">
  <div class="tab" style="width:138px">Mistakes Section</div>
  <svg class="tab-stripes" style="left:138px" width="26" height="23"><polygon points="0,0 6,0 16,23 10,23" fill="var(--navy)"/><polygon points="9,0 15,0 25,23 19,23" fill="var(--navy)"/></svg>
  <h2 class="abs h" style="left:19px;top:55px;font-size:10.5px">Mistake #1:<br>Misclassifying Employees</h2>
  <p class="abs body" style="left:19px;top:80px;width:300px;font-size:6.1px"><span class="label">Why it matters:</span> Misclassifying workers incorrectly is one of the most common—and expensive—mistakes contractors make. Whether it's assigning clerical codes to field workers or lumping all employees into a single category, misclassification can result in denied claims, audit penalties, backdated premium increases, or even regulatory fines. Insurance carriers determine your workers' comp rates based on the risk level associated with each job duty, so accuracy matters.</p>
  <div class="abs" style="left:19px;top:131px;width:301px;height:90px;border-radius:10px;overflow:hidden;background:var(--navy)">
    <div class="photo" role="img" aria-label="Insurance advisor reviewing a chart on a laptop with a client" style="left:0;top:0;width:142px;height:90px;background:linear-gradient(135deg,#b9a894 0%,#dfe3e8 45%,#8b8f96 100%)"></div>
    <div class="abs" style="left:158px;top:10px;width:130px">
      <div class="avoid-title" style="font-size:9.5px"><svg width="11" height="11" viewBox="0 0 11 11"><rect x="0.5" y="1.5" width="9" height="9" fill="none" stroke="var(--white)" stroke-width="0.9"/><path d="M2.5 6 L5 8.5 L10 0.5" fill="none" stroke="var(--teal)" stroke-width="1.3"/></svg>Avoid it:</div>
      <p style="margin-top:6px;color:var(--white);font-size:5px;line-height:7px;text-align:justify">Conduct regular reviews of employee job duties with your insurance broker, especially when roles change or new services are added. Make sure you're using the correct class codes as defined by your state's rating bureau or NRCB. When in doubt, ask your broker to help you confirm classifications before a policy is issued—or audited.</p>
    </div>
  </div>
  <div class="footer-brand"><span class="dot"></span>Brelwick</div>
  <div class="footer-line"></div><div class="page-num"></div>
</section>

<!-- Mistake 2 -->
<section class="page" style="left:72px;top:361px">
  <div class="tab" style="width:132px">Mistakes Section</div>
  <svg class="tab-stripes" style="left:132px" width="26" height="23"><polygon points="0,0 6,0 16,23 10,23" fill="var(--navy)"/><polygon points="9,0 15,0 25,23 19,23" fill="var(--navy)"/></svg>
  <h2 class="abs h" style="left:19px;top:47px;font-size:10.5px;line-height:11.5px">Mistake #2.<br>Not Collecting Certificates of Insurance (COIs)<br>from Subcontractors</h2>
  <p class="abs body" style="left:23px;top:99px;width:132px;font-size:6.1px"><span class="label" style="display:block">Why it matters:</span>If a subcontractor doesn't have their own active workers' comp policy, your business could be held liable for their injuries. This often results in surprise audit charges or even denied claims. Not collecting COIs can inflate your payroll exposure and raise red flags during audits.</p>
  <div class="photo" role="img" aria-label="Two people reviewing a contract at a table with a laptop" style="left:164px;top:89px;width:141px;height:84px;border-radius:9px;background:linear-gradient(135deg,#6d7784 0%,#d9dde2 50%,#3d4450 100%)"></div>
  <div class="abs avoid-title" style="left:23px;top:182px;font-size:9.5px"><svg width="12" height="12" viewBox="0 0 11 11"><rect x="0.5" y="1.5" width="9" height="9" fill="none" stroke="var(--navy)" stroke-width="0.9"/><path d="M2.5 6 L5 8.5 L10 0.5" fill="none" stroke="var(--teal)" stroke-width="1.3"/></svg>Avoid it:</div>
  <p class="abs" style="left:23px;top:199px;width:280px;font-size:5.1px;line-height:8.4px;color:#70747a">Always request and verify up-to-date COIs for every subcontractor before they step on site. Keep copies of COIs for your records and set calendar reminders to follow up on expirations. Your insurance broker can also help you implement a subcontractor tracking system.</p>
  <div class="footer-brand"><span class="dot"></span>Brelwick</div>
  <div class="footer-line"></div><div class="page-num"></div>
</section>

<!-- Mistake 10 -->
<section class="page" style="left:430px;top:361px">
  <div class="tab" style="width:147px">Mistakes Section</div>
  <svg class="tab-stripes" style="left:147px" width="26" height="23"><polygon points="0,0 6,0 16,23 10,23" fill="var(--navy)"/><polygon points="9,0 15,0 25,23 19,23" fill="var(--navy)"/></svg>
  <div class="photo" role="img" aria-label="Two construction workers in hard hats talking on a building site" style="left:27px;top:56px;width:114px;height:108px;border-radius:9px;background:linear-gradient(135deg,#c9cdd1 0%,#d8b06a 35%,#3a4d7a 70%,#c9a878 100%)"></div>
  <h2 class="abs h" style="left:155px;top:56px;font-size:10.5px;line-height:11.5px">Mistake #10:<br>Working with a Generalist<br>Broker</h2>
  <p class="abs body" style="left:155px;top:94px;width:162px;font-size:6.1px;line-height:9px"><span class="label" style="display:block">Why it matters:</span>Most insurance agents don't specialize in the Construction Industry. Workers' comp is complex—especially in construction. A generalist insurance agent may miss key exposures, costing you more in the long run. They may not know how to leverage safety programs, return-to-work strategies, or MOD improvement tactics.</p>
  <div class="abs" style="left:28px;top:175px;width:288px;height:48px;border-radius:8px;background:var(--navy);padding:6px 10px">
    <div class="avoid-title" style="font-size:9.5px"><svg width="12" height="12" viewBox="0 0 11 11"><rect x="0.5" y="1.5" width="9" height="9" fill="none" stroke="var(--white)" stroke-width="0.9"/><path d="M2.5 6 L5 8.5 L10 0.5" fill="none" stroke="var(--teal)" stroke-width="1.3"/></svg>Avoid it:</div>
    <p style="margin-top:4px;color:var(--white);font-size:5px;line-height:6.4px">Partner with an agency that specializes in workers' comp for contractors and understands your industry inside and out. A knowledgeable insurance advisor can help you avoid costly mistakes and build a safer, more insurable business. Choose a broker who specializes in Workers' Comp for contractors.</p>
  </div>
  <div class="footer-brand"><span class="dot"></span>Brelwick</div>
  <div class="footer-line"></div><div class="page-num"></div>
</section>

<!-- Call to action -->
<section class="page" style="left:790px;top:361px">
  <h2 class="abs h" style="left:27px;top:31px;font-size:12.5px;line-height:14px">Ready to Take<br>Control of Your Workers' Comp Costs?</h2>
  <p class="abs" style="left:27px;top:68px;font-family:'Montserrat',sans-serif;font-size:8.3px;line-height:10px;color:var(--navy)">Schedule your<br><b class="teal">FREE Workers' Comp Risk Assessment</b> today.</p>
  <div class="abs" style="left:0;top:99px;width:215px;height:65px;background:var(--teal);padding:6px 0 0 27px;color:var(--white);font-family:'Montserrat',sans-serif">
    <div style="font-size:8.8px;font-weight:700">Contact Us at</div>
    <div style="font-size:15px;font-weight:600;line-height:18px">(555) 014-2271</div>
    <div style="font-size:7px;line-height:8.5px;margin-top:3px">Visit us at<br><b>BrelwickInsurance.com</b> to learn more.</div>
  </div>
  <div class="abs" style="left:0;top:164px;width:225px;height:70px;background:var(--navy);padding:8px 0 0 27px;font-family:'Montserrat',sans-serif">
    <div style="display:flex;align-items:center;gap:4px;color:var(--white);font-weight:600;font-size:10px"><span class="dot" style="width:12px;height:12px;background:var(--white)"></span>Brelwick</div>
    <div style="font-size:8.8px;font-weight:700;color:var(--teal);margin-top:7px">Brelwick Insurance &amp; Consulting</div>
    <div style="font-size:6.4px;color:var(--white);line-height:8.6px">Construction Insurance Specialists<br>Licensed in OR | WA | NV</div>
  </div>
  <div class="photo" role="img" aria-label="Bearded construction worker in a white hard hat and hi-vis jacket looking upward" style="left:178px;top:83px;width:161px;height:179px;border-top-left-radius:80px 120px;background:linear-gradient(160deg,#f2efe9 0%,#b89a7c 35%,#6b4a34 65%,#d46a1e 100%)"></div>
</section>

</div>
</body>
</html>
```